Startup online payment business - Sporting / Golf, Swift Tee payment

Background:
Our business name is "Swift Tee" we provide online payments for golfing services via our website. We currently have a logo used on our website. No other design style has been developed. Our aim is to remove cash payments for service at golf clubs.

Our Key Values:
Quick and easy
Formal and polite
Fun with professional boundary
Mate-ship relationships
100% online digital

What we want from you:
Marketing design to be used on posters and stickers in a retail setting to direct customers to our online payment Chanel.
Design must incorporate attached logo, URL swifttee.com.au and our key values can act as a guide the type of design. We have used color Hex#007672 for logo background. We are open to use other colors.

Target Market(s)

Golf clubs and golf players

Industry/Entity Type

Golf Course

Font styles to use
Sans Serif

Requirements
Must have
• Directions to online payment via URL: swifttee.com.au
Nice to have
• We like the idea of the slogan: No Cash - No worries. Have attached home screen that will be available from URL link. Consideration if using mobile phone in image. Push the online payment and steps 1. Visit swifttee.com 2. Select club 3. Confirm payment
Should not have
• Cartoons

```html
<!DOCTYPE html>
<html lang="en">
<head>
<meta charset="utf-8">
<title>Swift Tee – No Cash, No Worries sticker</title>
<link rel="stylesheet" href="https://fonts.googleapis.com/css2?family=Montserrat:wght@500;600;700&display=swap">
<style>
  :root {
    --backdrop: #000000;
    --brand-green: #0a9a55;
    --paper: #ffffff;
  }
  html, body {
    margin: 0;
    padding: 0;
    overflow: hidden;
    background: var(--backdrop);
  }
  .canvas {
    position: relative;
    width: 1200px;
    height: 1000px;
    background: var(--backdrop);
    overflow: hidden;
    font-family: "Montserrat", sans-serif;
  }
  .sticker {
    position: absolute;
    inset: 0;
  }
  .sticker__url {
    font-family: "Montserrat", sans-serif;
    font-weight: 500;
    font-size: 84px;
    fill: var(--paper);
    letter-spacing: 1px;
  }
  .sticker__brand {
    font-family: "Montserrat", sans-serif;
    font-weight: 700;
    font-size: 104px;
    fill: var(--paper);
    letter-spacing: 4px;
  }
  .values {
    position: absolute;
    left: 200px;
    top: 604px;
    width: 800px;
    margin: 0;
    padding: 0;
    list-style: none;
    text-align: center;
    color: var(--brand-green);
  }
  .values__slogan {
    font-weight: 700;
    font-size: 52px;
    line-height: 66px;
    letter-spacing: 0.5px;
  }
  .values__item {
    font-weight: 600;
    font-size: 33px;
    line-height: 45px;
  }
</style>
</head>
<body>
  <main class="canvas">
    <svg class="sticker" width="1200" height="1000" viewBox="0 0 1200 1000" aria-label="Swift Tee round sticker">
      <defs>
        <clipPath id="lower-panel">
          <rect x="0" y="600" width="1200" height="400"/>
        </clipPath>
        <path id="url-arc" d="M 282 500 A 318 318 0 0 1 918 500"/>
      </defs>

      <circle class="sticker__disc" cx="600" cy="500" r="400" fill="var(--brand-green)"/>
      <circle class="sticker__ring" cx="600" cy="500" r="384" fill="none" stroke="var(--paper)" stroke-width="3"/>
      <circle class="sticker__panel" cx="600" cy="500" r="390" fill="var(--paper)" clip-path="url(#lower-panel)"/>

      <text class="sticker__url">
        <textPath href="#url-arc" startOffset="50%" text-anchor="middle">swifttee.com.au</textPath>
      </text>

      <text class="sticker__brand" x="600" y="520" text-anchor="middle">SWIFT TEE</text>
    </svg>

    <ul class="values">
      <li class="values__slogan">No Cash - No worries</li>
      <li class="values__item">Quick and easy - Formal and polite</li>
      <li class="values__item">Fun with professional boundary</li>
      <li class="values__item">Mate-ship relationships</li>
      <li class="values__item">100% online digital</li>
    </ul>
  </main>
</body>
</html>
```